Coralith Partners's New Branding
Anything the customer sees, we want to update
Coralith Partners's New Branding -
Creative Brief
Professional
Dorian Pelk, MCP
Director of Technology
418 West Alder Road Morton, IL 61552
dorian.pelk@coralithpt.example
www.coralithpt.example
In addition to branding our business cards, we're also looking to brand: 1) folders - two pockets w/ a slotted area on the left pocket to insert a business card 2) brochures - 8.5"x11" tri-fold brochure 3) letterhead 4) envelopes 5) sales proposal cover letter - Our logo and name - Presented to: "Customer's name" - Presented by: "our sales person(s)" - Title of presentation - our web address 6) powerpoint 7) binders (including spline) 8) cd label - Company's name we're presenting cd to - our logo and name - title of content on cd
Quote: "Our business is sustaining yours" Please layout the quote so that if we put a QR code on the back of the card in the future, it won't look out of place.

```html
<!DOCTYPE html>
<html lang="en">
<head>
<meta charset="utf-8">
<title>Coralith Partners – Presentation Slides</title>
<link rel="stylesheet" href="https://fonts.googleapis.com/css2?family=Crimson+Text:wght@400;600&family=Open+Sans:wght@400;600&display=swap">
<style>
  :root {
    --green-deep: #0b3b25;
    --green-mid: #14583a;
    --green-bright: #2f8a4e;
    --green-text: #4fa95f;
    --green-title: #7fc08a;
    --green-light: #d9ecd9;
    --grey-soft: #e9ecea;
    --white: #ffffff;
    --ink: #1d1d1d;
  }
  * { box-sizing: border-box; margin: 0; padding: 0; }
  html, body { width: 1200px; height: 480px; overflow: hidden; background: var(--white); }
  body { position: relative; font-family: "Crimson Text", Georgia, serif; }

  .slide { position: absolute; top: 20px; width: 540px; height: 370px; overflow: hidden; }

  /* Title slide */
  .slide--title {
    left: 25px;
    background: radial-gradient(ellipse at 70% 40%, var(--green-mid) 0%, var(--green-deep) 75%);
  }
  .world-map {
    position: absolute; left: 170px; top: 20px; width: 360px; height: 240px;
    background: radial-gradient(ellipse at 50% 50%, rgba(80,150,100,0.35) 0%, rgba(80,150,100,0.12) 55%, rgba(80,150,100,0) 80%);
  }
  .logo-card {
    position: absolute; left: 0; top: 8px; width: 288px; height: 104px;
    background: var(--white); border-radius: 0 12px 12px 0;
    display: flex; align-items: center; gap: 16px; padding-left: 26px;
  }
  .logo-dot { width: 40px; height: 40px; border-radius: 50%; background: var(--green-mid); flex: none; }
  .logo-name {
    font-family: "Crimson Text", Georgia, serif; font-weight: 600;
    font-size: 25px; letter-spacing: 2px; text-transform: uppercase; color: var(--green-deep);
    line-height: 1;
  }
  .presentation-title {
    position: absolute; left: 28px; bottom: 20px;
    font-size: 25px; color: var(--green-title);
  }

  /* Content slide */
  .slide--content { left: 580px; background: var(--white); border: 1px solid var(--grey-soft); }
  .content-band { position: absolute; left: 0; top: 0; width: 100%; height: 6px; background: var(--green-deep); }
  .content-logo { position: absolute; left: 20px; top: 20px; display: flex; align-items: center; gap: 10px; }
  .content-logo .logo-dot { width: 28px; height: 28px; }
  .content-logo .logo-name { font-size: 18px; }
  .swoosh {
    position: absolute; right: -80px; bottom: 10px; width: 300px; height: 220px;
    border-radius: 50%; background: var(--grey-soft); opacity: 0.7;
  }
  .section { position: absolute; left: 22px; width: 330px; }
  .section--one { top: 108px; }
  .section--two { top: 196px; }
  .section-heading { font-size: 17px; color: var(--green-mid); line-height: 1.1; margin-bottom: 3px; }
  .section-body { font-size: 9.5px; line-height: 1.3; color: var(--green-text); }
  .photo { position: absolute; }
  .photo--pipes {
    left: 383px; top: 25px; width: 117px; height: 115px;
    background: linear-gradient(135deg, #e4e6e3 0%, #b9bdb8 60%, #8e938e 100%);
  }
  .photo--growth {
    left: 365px; top: 182px; width: 155px; height: 138px;
    background: radial-gradient(ellipse at 55% 55%, #e6b94a 0%, #d9893a 45%, #f4f1ea 85%);
  }
  .footer-band {
    position: absolute; left: 0; bottom: 0; width: 100%; height: 26px;
    background: var(--green-deep); display: flex; align-items: center; padding-left: 22px;
  }
  .footer-url { font-family: "Open Sans", Arial, sans-serif; font-size: 9px; font-weight: 600; color: var(--white); }

  .caption {
    position: absolute; left: 0; width: 1200px; top: 428px; text-align: center;
    font-family: "Open Sans", Arial, sans-serif; font-size: 22px; color: var(--ink);
  }
</style>
</head>
<body>
  <section class="slide slide--title">
    <div class="world-map" role="img" aria-label="Faint world map in green tones"></div>
    <div class="logo-card">
      <span class="logo-dot"></span>
      <span class="logo-name">Coralith Partners</span>
    </div>
    <h1 class="presentation-title">Title of Presentation</h1>
  </section>

  <section class="slide slide--content">
    <div class="content-band"></div>
    <div class="swoosh"></div>
    <div class="content-logo">
      <span class="logo-dot"></span>
      <span class="logo-name">Coralith Partners</span>
    </div>
    <div class="section section--one">
      <h2 class="section-heading">Coralith Partners</h2>
      <p class="section-body">Coralith Partners delivers steady guidance for growing firms. Our advisors plan, review and protect every account with care, clear reporting and honest counsel so clients can focus on the work ahead.</p>
    </div>
    <div class="section section--two">
      <h2 class="section-heading">Coralith Partners</h2>
      <p class="section-body">We measure progress each quarter and share the results openly. Trusted service, sound planning and lasting partnerships remain the core of everything our team builds for you.</p>
    </div>
    <div class="photo photo--pipes" role="img" aria-label="Photo of stacked concrete pipes"></div>
    <div class="photo photo--growth" role="img" aria-label="Illustration of a rising chart over stacks of gold coins"></div>
    <div class="footer-band"><span class="footer-url">www.coralithpt.example</span></div>
  </section>

  <p class="caption">Powerpoint slides</p>
</body>
</html>
```